POOL BUILDING CONTRACTOR

our company has shifter focus over the past 18 month we no longer have a retail store and no longer clean pools we build concrete pools. our website if 5 years old we need a completely new site that shows our core product, building concrete pools & renovate concrete pools

here is a few of our competitors;
brantelwaters.com
okvimbuilders.com
ridgeviewlagoonworks.com
plunvora.com
halvertonbasinsandtubs.com
dremblewaterne.com

one we land on a final design I will upload customer before and after photos and any other content needed

Target Market(s)

People looking to build or renovate there pool

Industry/Entity Type

swimming pool

Coding

Coded - Design and coding required

Number of Pages Required

5+ page

Colors
0054AA
0677BA
7BADD7
CADEEF
E8F1F8

Requirements
Must have
• financing Service-Repairs & liners new build-photos renovate-remodeling design-consult customer-reviews Gallery Before-After Contact us 3D Design & Modeling construction process & Timeline Equipment Features Hardscapes I like these sites https://meadowlarkbasinsbycraft.com/ https://holtbergwaters.com/

```html
<!DOCTYPE html>
<html lang="en">
<head>
<meta charset="utf-8">
<title>Tidewell – The Pool Service Company</title>
<link href="https://fonts.googleapis.com/css2?family=Lato:wght@400;700;900&display=swap" rel="stylesheet">
<style>
:root{
  --topbar:#4e6482;
  --brand:#0c71c3;
  --brand-light:#2ea3f2;
  --navy:#0b3a73;
  --navy-dark:#13407a;
  --ink:#222;
  --white:#fff;
  --footer:#4e6482;
}
*{margin:0;padding:0;box-sizing:border-box}
html,body{width:1200px;height:2369px;overflow:hidden;background:var(--white);font-family:'Lato',sans-serif;color:var(--ink)}
.page{position:relative;width:1200px;height:2369px}
.topbar{position:absolute;top:0;left:0;width:1200px;height:29px;background:var(--topbar);color:var(--white);font-size:11px;font-weight:700}
.topbar .call{position:absolute;left:139px;top:8px;display:flex;align-items:center;gap:5px}
.topbar .social{position:absolute;left:487px;top:9px;display:flex;gap:12px}
.dot{width:10px;height:10px;border-radius:50%;background:var(--white);opacity:.9}
.topbar .links{position:absolute;right:138px;top:8px;display:flex;gap:14px}
.header{position:absolute;top:29px;left:0;width:1200px;height:89px;background:var(--white);box-shadow:0 1px 0 rgba(0,0,0,.08)}
.brand{position:absolute;left:25px;top:15px;display:flex;align-items:center;gap:8px}
.brand .mark{width:60px;height:60px;border:3px solid #3a5a86;background:#e8f1f8}
.brand .name{font-size:42px;font-weight:900;color:#3a5a86;letter-spacing:-1px}
.nav{position:absolute;left:529px;top:33px;display:flex;gap:18px;font-size:13px;font-weight:700}
.nav .active{color:var(--brand-light)}
.btn-request{position:absolute;left:1026px;top:33px;width:122px;height:38px;background:var(--brand);color:var(--white);font-size:13px;font-weight:700;display:flex;align-items:center;justify-content:center}
.search{position:absolute;left:1163px;top:45px}
.hero{position:absolute;top:118px;left:0;width:1200px;height:432px;background:linear-gradient(180deg,#6f9fc9 0%,#a8cbe6 30%,#4a9bd3 55%,#2f84c6 100%);text-align:center;color:var(--white)}
.hero .badge{position:absolute;left:568px;top:65px;width:64px;height:64px;background:var(--white);border:3px solid #3a5a86}
.hero h1{position:absolute;top:145px;width:100%;font-size:44px;font-weight:900}
.hero h2{position:absolute;top:216px;width:100%;font-size:28px;font-weight:700}
.hero p{position:absolute;top:253px;left:340px;width:520px;font-size:16px;line-height:26px;opacity:.85}
.hero .learn{position:absolute;left:531px;top:317px;width:138px;height:51px;border-radius:26px;background:var(--navy);font-size:12px;font-weight:700;letter-spacing:1px;display:flex;align-items:center;justify-content:center}
.band{position:absolute;left:0;width:1200px;background:var(--brand);color:var(--white);text-align:center}
.band h3{font-size:23px;font-weight:700}
.band p{width:900px;margin:0 auto;font-size:13.5px;font-weight:700;line-height:21px}
.band-intro{top:550px;height:236px}
.band-intro h3{margin-top:77px;margin-bottom:16px}
.creations{position:absolute;top:786px;left:0;width:1200px;height:442px}
.creation{position:absolute;top:0;width:436px;text-align:center}
.creation h4{margin-top:76px;font-size:23px;font-weight:700;color:var(--brand)}
.video{position:relative;margin-top:38px;height:230px}
.video .controls{position:absolute;left:10px;right:10px;bottom:12px;color:var(--white);font-size:10px;font-weight:700;display:flex;align-items:center;gap:8px}
.video .track{position:absolute;left:11px;right:11px;bottom:14px;height:3px;background:rgba(255,255,255,.4)}
.video .track span{display:block;height:3px;background:rgba(255,255,255,.85)}
.band-expert{top:1228px;height:295px}
.band-expert h3{margin-top:76px;margin-bottom:16px}
.btn-contact{display:inline-block;margin-top:35px;padding:9px 15px;background:var(--white);color:var(--brand);font-size:14px;letter-spacing:1px}
.gallery{position:absolute;top:1523px;left:0;width:1200px;height:364px;text-align:center}
.gallery h4{margin-top:78px;font-size:23px;font-weight:700;color:var(--brand)}
.thumb{position:absolute;top:164px;width:192px;height:129px;border:2px solid var(--brand)}
.footer{position:absolute;top:1887px;left:0;width:1200px;height:281px;background:var(--footer);color:var(--white)}
.fcol{position:absolute;top:58px;font-size:12px}
.fcol h5{font-size:17px;font-weight:400;margin-bottom:7px}
.fcol ul{list-style:none}
.fcol li{position:relative;padding-left:11px;margin-bottom:7px;line-height:16px;width:100px}
.fcol li::before{content:"";position:absolute;left:0;top:7px;width:3px;height:3px;border-radius:50%;background:var(--white)}
.fcol.addr p{margin-bottom:8px;line-height:18px}
.flogo{position:absolute;left:794px;top:61px;width:98px;height:102px;background:var(--white);border:3px solid #dfe8f2}
.bottombar{position:absolute;top:2168px;left:0;width:1200px;height:39px;background:var(--navy-dark);color:var(--white);font-size:12px}
.bottombar .copy{position:absolute;left:139px;top:12px}
.bottombar .social{position:absolute;right:138px;top:13px;display:flex;gap:18px}
</style>
</head>
<body>
<div class="page">
  <div class="topbar">
    <div class="call">
      <svg width="10" height="10" viewBox="0 0 24 24"><path fill="#fff" d="M6.6 10.8a15 15 0 0 0 6.6 6.6l2.2-2.2c.3-.3.7-.4 1-.2 1.1.4 2.3.6 3.6.6.6 0 1 .4 1 1V20c0 .6-.4 1-1 1A17 17 0 0 1 3 4c0-.6.4-1 1-1h3.5c.6 0 1 .4 1 1 0 1.3.2 2.5.6 3.6.1.3 0 .7-.2 1z"/></svg>
      SCHEDULE YOUR CONSULTATION TODAY : (555) 014-2290
    </div>
    <div class="social" aria-label="Social links"><span class="dot"></span><span class="dot"></span><span class="dot"></span></div>
    <div class="links"><span>Hardscapes</span><span>Construction Process &amp; Timeline</span><span>Customer-Reviews</span></div>
  </div>

  <header class="header">
    <div class="brand"><span class="mark"></span><span class="name">Tidewell</span></div>
    <nav class="nav">
      <span class="active">Home</span><span>Financing</span><span>Services ⌄</span><span>Gallery</span><span>Features</span><span>Equipment</span><span>Contact us</span>
    </nav>
    <div class="btn-request">Service Request</div>
    <svg class="search" width="14" height="14" viewBox="0 0 14 14"><circle cx="8" cy="6" r="4.5" fill="none" stroke="#333" stroke-width="1.5"/><path d="M4.8 9.2 1.5 12.5" stroke="#333" stroke-width="1.5"/></svg>
  </header>

  <section class="hero" role="img" aria-label="Infinity pool with chrome ladder overlooking the sea under a bright sky">
    <div class="badge"></div>
    <h1>TIDEWELL</h1>
    <h2>The Pool Service Company</h2>
    <p>Lorem ipsum dolor sit amet, consectetuer adipiscing elit. Cum sociis natoque penatibus et magnis dis parturient.</p>
    <div class="learn">LEARN MORE</div>
  </section>

  <section class="band band-intro">
    <h3>CENTRAL FLORIDA’S #1 POOL BUILDING CONTRACTOR</h3>
    <p>We’ve streamlined our pool building process to ensure it is smooth, efficient and completely transparent. Composed of expert designers and builders, our professional crew manages the entire process from start to finish.</p>
  </section>

  <section class="creations">
    <div class="creation" style="left:139px">
      <h4>CUSTOM CREATION</h4>
      <div class="video" role="img" aria-label="Video of a curved backyard pool among palm trees" style="background:linear-gradient(180deg,#7a9a6a 0%,#5f7f55 45%,#3f8fb8 70%,#2a2a2a 100%)">
        <div class="controls"><span>▶</span><span>0:00 / 0:15</span></div>
        <div class="track"><span style="width:27%"></span></div>
      </div>
    </div>
    <div class="creation" style="left:626px">
      <h4>CUSTOM CREATION</h4>
      <div class="video" role="img" aria-label="Video of children running beside a resort pool" style="background:linear-gradient(180deg,#4d6a3e 0%,#a8b39a 35%,#3a8fa8 65%,#1e2a2a 100%)">
        <div class="controls"><span>▶</span><span>0:00 / 0:07</span></div>
        <div class="track"><span style="width:43%"></span></div>
      </div>
    </div>
  </section>

  <section class="band band-expert">
    <h3>SPEAK TO A DESIGN EXPERT</h3>
    <p>We’ve streamlined our pool building process to ensure it is smooth, efficient and completely transparent. Composed of expert designers and builders, our professional crew manages the entire process from start to finish.</p>
    <span class="btn-contact">CONTACT US</span>
  </section>

  <section class="gallery">
    <h4>Project Gallery</h4>
    <div class="thumb" style="left:139px;background:linear-gradient(160deg,#8fb6d8,#4f7a3f 40%,#1d4f8a 70%,#a0563a)" role="img" aria-label="Villa pool with wooden deck"></div>
    <div class="thumb" style="left:383px;background:linear-gradient(160deg,#9cc0e0,#5a8348 40%,#2d6fa8 65%,#8a4a32)" role="img" aria-label="Garden pool beside a modern house"></div>
    <div class="thumb" style="left:626px;background:linear-gradient(180deg,#d9e4ef,#c9c6c0 45%,#6ab6d9 75%,#b9b5ad)" role="img" aria-label="Rectangular pool behind a white house"></div>
    <div class="thumb" style="left:869px;background:linear-gradient(135deg,#7fc3ea,#2f8fd2 60%,#1b6fb8)" role="img" aria-label="Pool ladder over blue tiled water"></div>
  </section>

  <footer class="footer">
    <div class="fcol" style="left:139px"><h5>Services</h5><ul><li>About Us</li><li>Hardscapes</li><li>Features</li><li>Equipment</li></ul></div>
    <div class="fcol" style="left:301px"><h5>Quick Link</h5><ul><li>About Us</li><li>Hardscapes</li><li>Features</li><li>Equipment</li></ul></div>
    <div class="fcol" style="left:463px;top:58px"><ul><li>Construction Process &amp; Timeline</li><li>3D Design &amp; Modeling</li><li>Contact us</li><li>Before-After</li></ul></div>
    <div class="fcol" style="left:625px;top:58px"><ul><li>Gallery</li><li>Before-After</li><li>Customer-Reviews</li><li>Financing</li></ul></div>
    <div class="flogo"></div>
    <div class="fcol addr" style="left:950px"><h5>Location</h5><p>Location<br>Tidewell Pools, Inc.<br>418 Harbor Pine Rd</p><p>Ocala, FL<br>34471</p><p>(555) 014-2290</p></div>
  </footer>

  <div class="bottombar">
    <span class="copy">Copyright © 2023 Tidewell</span>
    <div class="social" aria-label="Social links"><span class="dot"></span><span class="dot"></span><span class="dot"></span></div>
  </div>
</div>
</body>
</html>
```